HVACR truck and trailer wrap

I own Halvor air conditioning and refrigeration company and am interested in wrapping my vehicles and trailer. Currently I have a logo but am not opposed to other ideas. My aim is to be noticed while looking clean, simple and very professional. I sell venmark equipment so I would like a venmark logo somewhere in the wrap. If any further questions please email me at Tobiashlv7@quillpost.net.

HVACR

```html
<!DOCTYPE html>
<html lang="en">
<head>
<meta charset="utf-8">
<title>Halvor Air &amp; Refrig. — Trailer Wrap</title>
<link rel="stylesheet" href="https://fonts.googleapis.com/css2?family=Open+Sans:wght@400;600;800&display=swap">
<style>
  :root {
    --panel-black: #07090d;
    --panel-sheen: #1b2230;
    --ice-deep: #173a78;
    --ice-mid: #2c63b4;
    --ice-light: #6fc8f2;
    --heading-blue: #6cc5ee;
    --white: #ffffff;
    --phone-orange: #f47a1f;
    --flame-red: #e2231a;
    --flame-orange: #f7941d;
    --flame-yellow: #ffd200;
  }
  * { box-sizing: border-box; margin: 0; padding: 0; }
  html, body {
    width: 1200px; height: 898px; overflow: hidden;
    background: var(--panel-black);
    font-family: "Open Sans", sans-serif;
  }
  .wrap-panel {
    position: relative; width: 1200px; height: 898px; overflow: hidden;
    background: linear-gradient(160deg, var(--panel-sheen) 0%, var(--panel-black) 45%, var(--panel-black) 100%);
  }
  .ice-band {
    position: absolute; left: 0; right: 0; top: 470px; height: 320px;
    background: linear-gradient(180deg, rgba(44,99,180,0.85) 0%, rgba(23,58,120,0.9) 60%, rgba(7,9,13,0) 100%);
  }
  .logo-art-flames {
    position: absolute; left: 60px; top: 20px; width: 560px; height: 330px;
    border-radius: 48% 48% 20% 20%;
    background: radial-gradient(ellipse at 50% 85%, var(--flame-yellow) 0%, var(--flame-orange) 35%, var(--flame-red) 65%, rgba(226,35,26,0) 100%);
  }
  .logo-art-ice {
    position: absolute; left: 30px; top: 470px; width: 600px; height: 260px;
    border-radius: 40% 40% 50% 50%;
    background: radial-gradient(ellipse at 50% 40%, #bfe9fb 0%, var(--ice-light) 40%, #0f8fd6 75%, rgba(15,143,214,0) 100%);
  }
  .brand-name {
    position: absolute; left: 60px; width: 560px; text-align: center;
    color: var(--white); font-weight: 800; line-height: 1;
  }
  .brand-name--main { top: 290px; font-size: 136px; letter-spacing: -2px; }
  .brand-name--sub  { top: 440px; font-size: 50px; }
  .service-copy {
    position: absolute; left: 600px; width: 580px; text-align: center;
  }
  .service-copy__headline {
    top: 240px; color: var(--heading-blue); font-weight: 800;
    font-size: 55px; line-height: 1.2;
  }
  .service-copy__trade {
    top: 480px; color: var(--white); font-weight: 600; font-size: 30px;
  }
  .contact-phone {
    position: absolute; left: 685px; top: 560px;
    display: flex; align-items: center; gap: 18px;
    color: var(--phone-orange); font-weight: 400; font-size: 66px; line-height: 1;
  }
  .contact-phone__icon { width: 56px; height: 56px; flex: none; }
  .license-list {
    position: absolute; right: 40px; top: 795px; text-align: right;
    color: var(--white); font-size: 20px; line-height: 1.3;
  }
</style>
</head>
<body>
  <main class="wrap-panel">
    <div class="ice-band" role="img" aria-label="Blue ice cube pattern band across the lower panel"></div>
    <div class="logo-art-flames" role="img" aria-label="Flame illustration above the company name"></div>
    <div class="logo-art-ice" role="img" aria-label="Ice cubes resting in a blue water splash below the company name"></div>

    <p class="brand-name brand-name--main">Halvor</p>
    <p class="brand-name brand-name--sub">Air &amp; Refrig.</p>

    <h1 class="service-copy service-copy__headline" style="position:absolute">Repairs, Maintenance<br>and Installations</h1>
    <p class="service-copy service-copy__trade" style="position:absolute">Air Conditioning and Refrigeration</p>

    <p class="contact-phone">
      <svg class="contact-phone__icon" viewBox="0 0 56 56" aria-hidden="true">
        <circle cx="28" cy="28" r="28" fill="var(--phone-orange)"/>
        <path d="M20 14c2 0 3 1 4 4l1 4c0 2-1 3-3 4 1 4 4 7 8 8 1-2 2-3 4-3l4 1c3 1 4 2 4 4v3c0 2-2 4-5 4-12-1-22-11-23-23 0-3 2-6 6-6z" fill="var(--white)"/>
        <path d="M33 16a9 9 0 0 1 8 8M33 10a15 15 0 0 1 14 14" stroke="var(--white)" stroke-width="3" fill="none" stroke-linecap="round"/>
      </svg>
      555-014-3826
    </p>

    <p class="license-list">FL CA C041958<br>GA CN 007315</p>
  </main>
</body>
</html>
```